Business Card design for law firm = Juriskite Australia

We are seeking a new design for our business cards.
We are keeping our logo, which is attached.
We need space for
Name
Title
Address is , which is
Level 14
82 Penhallow Street
Sydney NSW 2000
Phone :
Mobile :
Fax :
Email :
DX :
website www.juriskite.com.au

Industry/Entity Type

Law Firm / Banking and Finance

Contact Information for Business Card

We are seeking a new design for our business cards. We are keeping our logo. We need space for Name Title Address is Level 14 82 Penhallow Street Sydney NSW 2000 Phone Mobile Fax Email DX website www.juriskite.com.au

Colors
0054AA
0677BA
7BADD7
CADEEF
E8F1F8

Requirements
Must have
• see our website for general feel www.juriskite.com.au

```html
<!DOCTYPE html>
<html lang="en">
<head>
<meta charset="utf-8">
<title>Juriskite Australia – Business Card</title>
<link href="https://fonts.googleapis.com/css2?family=Mulish:wght@400;700&display=swap" rel="stylesheet">
<style>
  :root {
    --backdrop: #aaaaaa;
    --navy-deep: #00204e;
    --navy-band: #042b57;
    --navy-back: #042d58;
    --navy-back-band: #00214d;
    --accent: #0a8fc0;
    --accent-text: #0b80b5;
    --white: #ffffff;
  }
  * { margin: 0; padding: 0; box-sizing: border-box; }
  html, body {
    width: 1200px; height: 1000px; overflow: hidden;
    background: var(--backdrop);
    font-family: "Mulish", "Avenir Next", sans-serif;
    color: var(--white);
  }
  .card {
    position: absolute;
    width: 515px; height: 297px;
    overflow: hidden;
  }
  .card__texture { position: absolute; inset: 0; }
  .card--front { left: 341px; top: 146px; background: var(--navy-deep); }
  .card--front .card__texture {
    background: linear-gradient(180deg, var(--navy-deep) 0%, var(--navy-band) 45%, var(--navy-deep) 75%, var(--navy-band) 100%);
  }
  .card--back { left: 342px; top: 494px; background: var(--navy-back); }
  .card--back .card__texture {
    background: linear-gradient(180deg, var(--navy-back) 0%, var(--navy-back-band) 20%, var(--navy-back) 30%, var(--navy-back) 100%);
  }

  .brand__square {
    position: absolute; left: 59px; top: 97px;
    width: 64px; height: 64px; background: var(--accent);
  }
  .brand__name {
    position: absolute; left: 58px; top: 172px;
    font-size: 38px; font-weight: 400; letter-spacing: 0.2px;
    line-height: 1;
  }
  .brand__tagline {
    position: absolute; left: 59px; top: 222px;
    font-size: 14px; color: var(--accent-text); letter-spacing: 0.6px;
  }

  .person { position: absolute; left: 59px; top: 98px; }
  .person__name { font-size: 17px; font-weight: 700; letter-spacing: 0.3px; line-height: 22px; }
  .person__title { font-size: 14px; letter-spacing: 0.3px; line-height: 18px; margin-left: 1px; }
  .person__rule { width: 79px; height: 3px; background: var(--accent); margin-top: 6px; }

  .contact {
    position: absolute; top: 180px;
    font-size: 12px; line-height: 14.5px; list-style: none;
  }
  .contact--details { left: 58px; }
  .contact--address { left: 318px; }
  .contact__web {
    margin-top: 14.5px; color: var(--accent); font-weight: 700;
  }
</style>
</head>
<body>
  <section class="card card--front" aria-label="Card front">
    <div class="card__texture" role="img" aria-label="Decorative flowing band pattern in navy tones"></div>
    <div class="brand__square" aria-hidden="true"></div>
    <div class="brand__name">Juriskite</div>
    <div class="brand__tagline">strategic legal outsourcing</div>
  </section>

  <section class="card card--back" aria-label="Card back">
    <div class="card__texture" role="img" aria-label="Decorative flowing band pattern in navy tones"></div>
    <div class="person">
      <div class="person__name">Marion Achterberg</div>
      <div class="person__title">Chief Legal Officer</div>
      <div class="person__rule"></div>
    </div>
    <ul class="contact contact--details">
      <li>P: 02 9184 0370</li>
      <li>M:</li>
      <li>F: 02 9184 0371</li>
      <li>E: enquiries@juriskite.com.au</li>
      <li>DX: 318 Sydney</li>
    </ul>
    <ul class="contact contact--address">
      <li>Level 14</li>
      <li>82 Penhallow Street</li>
      <li>Sydney NSW 2000</li>
      <li class="contact__web">www.juriskite.com.au</li>
    </ul>
  </section>
</body>
</html>
```